Vodka bottle label for premium caribbean market

Label design for a Vodka bottle
Vodka name is 742 Vodka
General colors desired are red and blue
This is a premium vodka product that will be made and distributed in the Caribbean
The art in the background are used in religious celebrations and need to be incorporated
The 742 Vodka design is what I personally created and want to follow a similar art design
Logo should say 742 Vodka
Updates

Reason: I was out on leave for personal reasons but ready to make a decision as soon as possible.

Target Market(s)

Premium vodka

Industry/Entity Type

Product

Logo Text

742 Vodka

Font styles to use
Other font styles liked:
• French Script MT

Colors
ec1f27
3176b5

Requirements
Must have
• Incorporate the name 742 Vodka
• Incorporate the 4 art designs as attached
• Font type is provided as an example
• 742 = French Script MT
• Vodka = Footlight MT light
Nice to have
• N/A
Should not have
• N/A

```html
<!DOCTYPE html>
<html lang="en">
<head>
<meta charset="utf-8">
<title>742 Vodka — Label Series</title>
<link rel="stylesheet" href="https://fonts.googleapis.com/css2?family=Playfair+Display:wght@700&display=swap">
<style>
  :root{
    --red:#ec1f27;
    --blue:#3176b5;
    --deep-red:#c4141b;
    --deep-blue:#2a5f9a;
    --gold:#f2b632;
    --gold-light:#ffe07a;
    --gold-dark:#b8760e;
    --paper:#ffffff;
  }
  html,body{margin:0;padding:0;overflow:hidden;}
  body{width:1200px;height:1068px;background:var(--paper);position:relative;}
  .label-row{
    position:absolute;left:50px;top:299px;
    width:1100px;height:470px;
    display:flex;gap:60px;
  }
  .label{position:relative;width:230px;height:470px;overflow:hidden;}
  .label svg.label-art{position:absolute;inset:0;width:100%;height:100%;}
  .brand{
    position:absolute;left:0;right:0;top:96px;
    display:flex;flex-direction:column;align-items:center;
    font-family:"Playfair Display",serif;font-weight:700;
    color:var(--gold);
  }
  .brand .numeral{display:flex;flex-direction:column;align-items:center;}
  .brand .digit{font-size:86px;line-height:74px;}
  .brand .premium{
    font-size:11px;line-height:14px;letter-spacing:5px;
    margin-top:14px;padding-left:5px;
  }
  .brand .word{font-size:34px;line-height:40px;letter-spacing:1px;margin-top:2px;}
  .label--stripes .brand{color:var(--paper);}
  .label--island .brand{top:158px;}
  .label--island .brand .digit{font-size:74px;line-height:64px;}
</style>
</head>
<body>
<main class="label-row">

  <!-- Label 1: red with blue pinstripes -->
  <section class="label label--stripes">
    <svg class="label-art" viewBox="0 0 230 470" aria-hidden="true">
      <defs>
        <pattern id="pinstripe" width="14" height="470" patternUnits="userSpaceOnUse">
          <rect width="14" height="470" fill="var(--red)"/>
          <rect x="4" width="6" height="470" fill="var(--blue)"/>
        </pattern>
      </defs>
      <rect width="230" height="470" fill="url(#pinstripe)"/>
    </svg>
    <svg class="label-art" viewBox="0 0 230 470">
      <rect x="30" y="90" width="170" height="240" rx="20" fill="var(--gold)" opacity="0.18" role="img" aria-label="Gold ceremonial veve ornaments"/>
    </svg>
    <div class="brand">
      <div class="numeral"><span class="digit">7</span><span class="digit">4</span><span class="digit">2</span></div>
      <span class="premium">PREMIUM</span>
      <span class="word">VODKA</span>
    </div>
  </section>

  <!-- Label 2: blue edges, red centre, gold side bands -->
  <section class="label label--radiant">
    <svg class="label-art" viewBox="0 0 230 470" aria-hidden="true">
      <defs>
        <radialGradient id="glow2" cx="0.5" cy="0.45" r="0.7">
          <stop offset="0.2" stop-color="var(--red)"/>
          <stop offset="1" stop-color="var(--blue)"/>
        </radialGradient>
        <linearGradient id="goldBand" x1="0" x2="1">
          <stop offset="0" stop-color="var(--gold-dark)"/>
          <stop offset="0.5" stop-color="var(--gold-light)"/>
          <stop offset="1" stop-color="var(--gold-dark)"/>
        </linearGradient>
      </defs>
      <rect width="230" height="470" fill="url(#glow2)"/>
      <rect x="0" width="14" height="470" fill="url(#goldBand)"/>
      <rect x="216" width="14" height="470" fill="url(#goldBand)"/>
    </svg>
    <svg class="label-art" viewBox="0 0 230 470">
      <rect x="28" y="40" width="174" height="290" rx="24" fill="var(--gold)" opacity="0.2" role="img" aria-label="Gold ceremonial veve ornaments"/>
    </svg>
    <div class="brand">
      <div class="numeral"><span class="digit">7</span><span class="digit">4</span><span class="digit">2</span></div>
      <span class="premium">PREMIUM</span>
      <span class="word">VODKA</span>
    </div>
  </section>

  <!-- Label 3: red centre, blue sides, thin gold borders -->
  <section class="label label--radiant-slim">
    <svg class="label-art" viewBox="0 0 230 470" aria-hidden="true">
      <defs>
        <linearGradient id="glow3" x1="0" x2="1">
          <stop offset="0" stop-color="var(--blue)"/>
          <stop offset="0.3" stop-color="var(--red)"/>
          <stop offset="0.7" stop-color="var(--red)"/>
          <stop offset="1" stop-color="var(--blue)"/>
        </linearGradient>
      </defs>
      <rect width="230" height="470" fill="url(#glow3)"/>
      <rect x="0" width="6" height="470" fill="var(--gold)"/>
      <rect x="224" width="6" height="470" fill="var(--gold)"/>
    </svg>
    <svg class="label-art" viewBox="0 0 230 470">
      <rect x="28" y="40" width="174" height="290" rx="24" fill="var(--gold)" opacity="0.2" role="img" aria-label="Gold ceremonial veve ornaments"/>
    </svg>
    <div class="brand">
      <div class="numeral"><span class="digit">7</span><span class="digit">4</span><span class="digit">2</span></div>
      <span class="premium">PREMIUM</span>
      <span class="word">VODKA</span>
    </div>
  </section>

  <!-- Label 4: red to blue with island medallion -->
  <section class="label label--island">
    <svg class="label-art" viewBox="0 0 230 470" aria-hidden="true">
      <defs>
        <linearGradient id="glow4" x1="0" y1="0" x2="0" y2="1">
          <stop offset="0" stop-color="var(--blue)"/>
          <stop offset="0.35" stop-color="var(--red)"/>
          <stop offset="0.8" stop-color="var(--deep-red)"/>
          <stop offset="1" stop-color="var(--deep-blue)"/>
        </linearGradient>
        <linearGradient id="goldBand4" x1="0" x2="1">
          <stop offset="0" stop-color="var(--gold-dark)"/>
          <stop offset="0.5" stop-color="var(--gold-light)"/>
          <stop offset="1" stop-color="var(--gold-dark)"/>
        </linearGradient>
      </defs>
      <rect width="230" height="470" fill="url(#glow4)"/>
      <rect x="0" width="14" height="470" fill="url(#goldBand4)"/>
      <rect x="216" width="14" height="470" fill="url(#goldBand4)"/>
    </svg>
    <svg class="label-art" viewBox="0 0 230 470">
      <defs>
        <linearGradient id="islandTone" x1="0" y1="0" x2="0" y2="1">
          <stop offset="0" stop-color="#7cc6ee"/>
          <stop offset="0.6" stop-color="#2f9fcf"/>
          <stop offset="1" stop-color="#e9d28a"/>
        </linearGradient>
      </defs>
      <ellipse cx="115" cy="82" rx="66" ry="58" fill="var(--gold)"/>
      <ellipse cx="115" cy="82" rx="60" ry="52" fill="url(#islandTone)" role="img" aria-label="Tropical island scene with palm trees and sailboat"/>
      <rect x="30" y="150" width="170" height="200" rx="24" fill="var(--gold)" opacity="0.2" role="img" aria-label="Gold ceremonial veve ornaments"/>
    </svg>
    <div class="brand">
      <div class="numeral"><span class="digit">7</span><span class="digit">4</span><span class="digit">2</span></div>
      <span class="premium">PREMIUM</span>
      <span class="word">VODKA</span>
    </div>
  </section>

</main>
</body>
</html>
```